Luxury Eco accommodation needs new website

Luxury lodge accommodation on exclusive private property in Flinders Ranges South Australia.
Brand new venture needs new site.
Focus on small group accommodation on exclusive property with outdoor experiences. Mountain biking , bush walking, outdoor dining.
We currently have a website but are having trouble making it our own. Needs to be "polished" by a professional.
Can you help?

www.larkhollowretreat.com.au

Target Market(s)

High income travellers, luxury accommodation

Industry/Entity Type

Accommodation

```html
<!DOCTYPE html>
<html lang="en">
<head>
<meta charset="utf-8">
<title>Lark Hollow Retreat – Contact</title>
<link href="https://fonts.googleapis.com/css2?family=Carlito:wght@400;700&display=swap" rel="stylesheet">
<style>
  :root{
    --header-top:#6c6f72;
    --header-bottom:#818487;
    --page-bg:#e5e5e5;
    --footer-bg:#707376;
    --nav-text:#cfcfcf;
    --body-text:#6b6b6b;
    --footer-text:#d2d2d2;
    --field-border:#7d7d7d;
    --button-bg:#787a7d;
    --button-text:#dcdcdc;
    --divider:#b5b5b5;
    --map-tone:#ddd8cc;
    --logo-ink:#3f3f3f;
    --white:#ffffff;
  }
  *{box-sizing:border-box;margin:0;padding:0}
  html,body{width:1200px;height:900px;overflow:hidden}
  body{font-family:"Carlito",Calibri,Arial,sans-serif;background:var(--page-bg);position:relative}

  .site-header{position:absolute;left:0;top:0;width:1200px;height:198px;
    background:linear-gradient(var(--header-top),var(--header-bottom))}
  .brand-logo{position:absolute;left:101px;top:73px;width:164px;height:104px;background:var(--white);
    display:flex;flex-direction:column;align-items:center;justify-content:center;gap:8px}
  .brand-logo .mark{width:14px;height:14px;background:var(--logo-ink)}
  .brand-logo .name{color:var(--logo-ink);font-size:15px;letter-spacing:1.5px;text-align:center;line-height:1.15}
  .greeting{position:absolute;right:101px;top:34px;color:var(--nav-text);font-weight:700;font-size:19px}
  .main-nav{position:absolute;right:101px;top:69px;color:var(--nav-text);font-weight:700;font-size:19px;word-spacing:1px}

  .location-map{position:absolute;left:104px;top:249px;width:337px;height:187px;background:var(--map-tone);
    border:1px solid #9a9a9a;box-shadow:2px 3px 4px rgba(0,0,0,.35)}
  .booking-info{position:absolute;left:103px;top:465px;color:var(--body-text);font-size:20px;line-height:25.5px}
  .booking-info h3{font-weight:700;font-size:20px}

  .column-divider{position:absolute;left:598px;top:250px;width:1px;height:266px;background:var(--divider)}

  .contact-form{position:absolute;left:660px;top:248px;color:var(--body-text)}
  .contact-form h2{font-size:19px;font-weight:700;margin-bottom:26px}
  .field{position:absolute;left:0;font-size:19px}
  .input{position:absolute;left:98px;width:202px;height:18px;border:1px solid var(--field-border)}
  .message-box{position:absolute;left:98px;top:152px;width:282px;height:100px;border:1px solid var(--field-border)}
  .send-button{position:absolute;left:98px;top:262px;width:150px;height:30px;background:var(--button-bg);
    color:var(--button-text);font-weight:700;font-size:18px;text-align:center;line-height:29px;
    box-shadow:3px 3px 3px rgba(0,0,0,.3)}

  .site-footer{position:absolute;left:0;top:600px;width:1200px;height:300px;background:var(--footer-bg);
    color:var(--footer-text);font-size:19px;line-height:25.2px}
  .footer-col{position:absolute;top:44px}
  .footer-col.primary{left:101px}
  .footer-col.support{left:422px}
  .footer-col.address{left:779px}
  .footer-col h4{font-weight:700;font-size:20px;letter-spacing:.5px}
  .social-links{display:flex;gap:3px;margin-top:8px}
  .social-links span{width:33px;height:33px;border-radius:5px;background:#ececec;border:1px solid #9a9a9a}
  .copyright{position:absolute;left:0;width:1200px;top:266px;text-align:center;font-size:19px}
</style>
</head>
<body>
  <header class="site-header">
    <div class="brand-logo">
      <span class="mark"></span>
      <span class="name">LARK HOLLOW<br>RETREAT</span>
    </div>
    <div class="greeting">Hi, Guest</div>
    <nav class="main-nav">LUXURY LODGE I OTHER STAYS I EXPERIENCES I GALLERY I CONTACT</nav>
  </header>

  <div class="location-map" role="img" aria-label="Street map showing the retreat's location"></div>

  <section class="booking-info">
    <h3>For Bookings &amp; Information:</h3>
    <p>Ph-&nbsp; (08) 8641 2290</p>
    <p>E-mail- stay@larkhollowretreat.com.au</p>
  </section>

  <div class="column-divider"></div>

  <section class="contact-form">
    <h2>CONTACT US:</h2>
    <span class="field" style="top:50px">Name:</span><span class="input" style="top:52px"></span>
    <span class="field" style="top:75px">MobileNo:</span><span class="input" style="top:77px"></span>
    <span class="field" style="top:100px">E-Mail:</span><span class="input" style="top:102px"></span>
    <span class="field" style="top:126px">Subject:</span><span class="input" style="top:128px"></span>
    <span class="field" style="top:151px">Massage:</span><span class="message-box"></span>
    <span class="send-button">Send Message</span>
  </section>

  <footer class="site-footer">
    <div class="footer-col primary">
      <p>LUXURY LODGE</p><p>OTHER STAYS</p><p>EXPERIENCES</p><p>GALLERY</p><p>CONTACT</p>
    </div>
    <div class="footer-col support">
      <p>FEEDBACK</p><p>HELP</p><p>FAQ</p><p>SUPPORT</p>
      <div class="social-links"><span></span><span></span><span></span></div>
    </div>
    <div class="footer-col address">
      <h4>LARK HOLLOW RETREAT</h4>
      <p>STONE GATE,</p><p>4TH ROAD N/E</p><p>HAWKER.</p><p>SOUTH AUSTRALIA</p>
      <p>PH- (08) 8641 7730</p><p>E-MAIL- info@larkhollowretreat.com.au</p>
    </div>
    <p class="copyright">Copyright © 2013 Lark Hollow Retreat</p>
  </footer>
</body>
</html>
```